Need a professional card design. Tallowmere building company specialise in residential and commercial builds. New homes, additions & renovations.
Wanting a card with creativity and professionalism.
Want card that utilises logo.

Back and front.

I have just created a logo, and want to use it on the business card.
Attached a copy of the logo.
Attached is also a current business card which I wish to redesign

please utilise both sides

Residential

• Reg# 58306

```html
<!DOCTYPE html>
<html lang="en">
<head>
<meta charset="utf-8">
<title>Tallowmere Building Co — Business Card</title>
<link rel="stylesheet" href="https://fonts.googleapis.com/css2?family=Cinzel:wght@400;600&family=Tinos&display=swap">
<style>
  :root {
    --stage: #e9e6e2;
    --card-dark: #231f1e;
    --card-light: #ffffff;
    --amber: #eea637;
    --ink: #1d1b1a;
    --paper-text: #f4f1ec;
  }
  * { box-sizing: border-box; margin: 0; padding: 0; }
  html, body { width: 1200px; height: 1000px; overflow: hidden; }
  body { background: var(--stage); position: relative; font-family: "Tinos", serif; }

  .card {
    position: absolute; left: 250px; width: 700px; height: 376px;
    box-shadow: 0 8px 24px rgba(0,0,0,.18);
  }
  .card--front { top: 90px; background: var(--card-dark); }
  .card--back { top: 534px; background: var(--card-light); }

  .brand {
    position: absolute; left: 0; right: 0; text-align: center;
    font-family: "Cinzel", serif; font-weight: 600; color: var(--amber);
    letter-spacing: 1px; display: flex; justify-content: center; align-items: center; gap: 14px;
  }
  .brand__dot { width: 16px; height: 16px; border-radius: 50%; background: var(--amber); }
  .card--front .brand { top: 140px; font-size: 40px; }
  .card--back .brand { top: 70px; font-size: 40px; }

  .tagline {
    position: absolute; left: 0; right: 0; top: 296px;
    display: flex; align-items: center; gap: 10px;
  }
  .tagline__rule { flex: 1; height: 5px; border-top: 1.5px solid var(--amber); border-bottom: 1.5px solid var(--amber); }
  .tagline__text {
    font-family: "Cinzel", serif; color: var(--paper-text); font-size: 14px;
    letter-spacing: 2.6px; white-space: nowrap;
  }

  .person { position: absolute; left: 42px; top: 216px; text-align: right; font-family: "Cinzel", serif; }
  .person__name { font-size: 26px; letter-spacing: 1px; color: var(--ink); }
  .person__name .first { color: var(--amber); }
  .person__role { font-size: 13px; letter-spacing: 3px; color: var(--ink); margin-top: -2px; }

  .contacts { position: absolute; left: 322px; top: 224px; list-style: none; font-size: 15.5px; color: var(--ink); }
  .contacts li { display: flex; align-items: center; gap: 8px; height: 25px; }
  .contacts svg { width: 18px; height: 18px; fill: var(--amber); flex: none; }

  .footer-rule {
    position: absolute; left: 0; right: 0; top: 340px; height: 6px;
    border-top: 1.5px solid var(--amber); border-bottom: 1.5px solid var(--amber);
  }
  .reg {
    position: absolute; left: 0; top: 346px; width: 176px; height: 30px;
    border-right: 1.5px solid var(--amber); padding: 7px 0 0 12px;
    font-family: "Cinzel", serif; font-size: 13px; letter-spacing: 2px; color: var(--ink);
  }
</style>
</head>
<body>
  <section class="card card--front" aria-label="Card front">
    <div class="brand"><span class="brand__dot"></span><span>Tallowmere Building Co</span></div>
    <div class="tagline">
      <span class="tagline__rule"></span>
      <span class="tagline__text">New homes, additions &amp; renovations</span>
      <span class="tagline__rule"></span>
    </div>
  </section>

  <section class="card card--back" aria-label="Card back">
    <div class="brand"><span class="brand__dot"></span><span>Tallowmere Building Co</span></div>

    <div class="person">
      <p class="person__name"><span class="first">Aurel</span> Vasile</p>
      <p class="person__role">Director</p>
    </div>

    <ul class="contacts">
      <li><svg viewBox="0 0 24 24"><path d="M3 8c0-2 3-4 9-4s9 2 9 4v2h-5V8H8v2H3zM6 11h12l3 9H3zm6 2a3 3 0 1 0 0 6 3 3 0 0 0 0-6z"/></svg>tel/fax: 08 9412 6170</li>
      <li><svg viewBox="0 0 24 24"><path d="M8 2h8a2 2 0 0 1 2 2v16a2 2 0 0 1-2 2H8a2 2 0 0 1-2-2V4a2 2 0 0 1 2-2zm0 3v11h8V5zm4 13a1.3 1.3 0 1 0 0 2.6 1.3 1.3 0 0 0 0-2.6z"/></svg>mob: 0422 518 903</li>
      <li><svg viewBox="0 0 24 24"><path d="M2 5h20v14H2zm2 2v.5l8 6 8-6V7zm0 3v7h16v-7l-8 6z"/></svg>email: tallowmerebuildingco@mailbox.com</li>
      <li><svg viewBox="0 0 24 24"><path d="M12 3l10 9h-3v9h-5v-6h-4v6H5v-9H2z"/></svg>42 Larkspur Way kinross WA 6029</li>
    </ul>

    <div class="footer-rule"></div>
    <p class="reg">Reg. no 58306</p>
  </section>
</body>
</html>
```